Business Card (double-sided) and Stationary Design for dental office

1) Business Card Design: We need a business card design for a dental specialty office.
Texts should contain:
The name of our office "Bayhaven Grins Orthodontics"
Tagline: "Specialist in Orthodontic and Maxillofacial Orthopedics"
Tag line: "Creating "Talvering" smiles for Children and Adults"
Doctor name: "Doctor Name"
Office Address:
"123 Street Name
City, State Zip code"
Office email address: office@bayhavengrins.com
Website: www.bayhavengrins.com

We will provide the full office address once the design is selected
Theme: beach, paradise, coastal, wave
We would like to have some creativity in design. Some acceptable ideas: front page: logo and office name. Back page: more detail information, and map to office in form of an island. Please see sample from our other location, but you DON'T HAVE TO USE OR COPY THE SAME CONCEPT.

IF POSSIBLE, PLEASE SUBMIT AT LEAST TWO CONCEPTS: ONE WITH THE BACK LOOKING SIMILAR TO WHAT IS IN THE SAMPLE, AND ONE DIFFERENT.

Color: designer to choose. We have different shade of blues and sand color in our office. Please see logo.

2) Please also design a matching set of stationary that compliment the business card and our logo.

Target Market(s)

Dental

Contact Information for Business Card

See descriptions

Font styles to use
Other font styles liked:
• Matching texts in logo

Colors
0054AA
0677BA
7BADD7
CADEEF
E8F1F8
0094D4
00A9DD
6FCCEA
C7EBF8
E9F6FB
00AB8E
00BBA5
67D7C9
C6EFE9
E9F9F6

Requirements
Must have
• Double-sided
Nice to have
• Beach coastal theme
Should not have
• Any shape or drawing of of tooth or teeth. We don’t need these. You don't necessarily have to just cut and paste the logo art and text as a whole, you have the liberty to rearrange the text.

```html
<!DOCTYPE html>
<html lang="en">
<head>
<meta charset="utf-8">
<title>Bayhaven Grins Orthodontics – Envelope</title>
<link rel="stylesheet" href="https://fonts.googleapis.com/css2?family=Jost:wght@700&family=Roboto+Slab:wght@400;700&display=swap">
<style>
  :root {
    --sea-green: #03ab90;
    --paper: #ffffff;
    --ink: #0b0b0b;
    --mark-teal: #417a8e;
    --bubble: #f3f7f6;
  }
  html, body {
    margin: 0;
    padding: 0;
    overflow: hidden;
    background: var(--sea-green);
  }
  .envelope {
    position: relative;
    width: 1200px;
    height: 825px;
    overflow: hidden;
    background: var(--sea-green);
  }
  .envelope-art {
    position: absolute;
    inset: 0;
  }
  .sender-mark {
    position: absolute;
    left: 63px;
    top: 580px;
    width: 154px;
    height: 154px;
    border-radius: 50%;
    background: var(--mark-teal);
  }
  .sender-block {
    position: absolute;
    left: 248px;
    top: 589px;
    color: var(--ink);
  }
  .practice-name {
    margin: 0;
    font-family: "Jost", sans-serif;
    font-weight: 700;
    font-size: 22px;
    letter-spacing: 0.6px;
    text-transform: uppercase;
    line-height: 1;
  }
  .doctor-name {
    margin: 17px 0 0;
    font-family: "Roboto Slab", serif;
    font-weight: 700;
    font-size: 19px;
    letter-spacing: 0.6px;
    text-transform: uppercase;
    line-height: 1;
  }
  .address,
  .contact-line {
    margin: 0;
    font-family: "Roboto Slab", serif;
    font-weight: 400;
    letter-spacing: 0.8px;
  }
  .address {
    margin-top: 15px;
    font-size: 18.5px;
    line-height: 1;
  }
  .contact {
    margin-top: 13px;
  }
  .contact-line {
    font-size: 18px;
    line-height: 25px;
  }
</style>
</head>
<body>
  <main class="envelope">
    <svg class="envelope-art" width="1200" height="825" viewBox="0 0 1200 825" aria-hidden="true">
      <defs>
        <filter id="bubble-shadow" x="-30%" y="-30%" width="160%" height="160%">
          <feDropShadow dx="0" dy="1" stdDeviation="2.5" flood-color="#000" flood-opacity="0.08"/>
        </filter>
      </defs>
      <path class="envelope-body" fill="var(--paper)"
            d="M12 14 L600 394 L1188 14 L1188 450
               C1170 490 1165 560 1158 640
               C1148 740 1110 790 1065 814
               L12 814 Z"/>
      <g class="bubbles" filter="url(#bubble-shadow)">
        <circle cx="591" cy="28" r="56" fill="#ffffff" fill-opacity="0.14"/>
        <circle cx="30" cy="153" r="56" fill="var(--bubble)" fill-opacity="0.7"/>
        <circle cx="576" cy="404" r="56" fill="var(--bubble)" fill-opacity="0.55"/>
        <circle cx="1183" cy="365" r="56" fill="var(--bubble)" fill-opacity="0.55"/>
        <circle cx="171" cy="544" r="56" fill="var(--bubble)" fill-opacity="0.7"/>
        <circle cx="859" cy="718" r="56" fill="var(--bubble)" fill-opacity="0.7"/>
      </g>
    </svg>

    <div class="sender-mark" aria-hidden="true"></div>

    <address class="sender-block" style="font-style: normal;">
      <p class="practice-name">Bayhaven Grins Orthodontics</p>
      <p class="doctor-name">Doctor Name</p>
      <p class="address">123 Street Name City, State Zip code</p>
      <div class="contact">
        <p class="contact-line">office@bayhavengrins.com</p>
        <p class="contact-line">www.bayhavengrins.com</p>
      </div>
    </address>
  </main>
</body>
</html>
```